Lens Harbor Teutonia Website - Photography and Films

We are looking for a design that expresses the friendly, open nature of our company Lens Harbor Teutonia, yet at the same time is professional looking and functional.

Lens Harbor Teutonia is a B2B focused operation that hires out multi-lingual camera crews (and equipment) throughout Germany and Europe. We also produce tv features and coporate films. Our unique selling point is that we are native English speakers who can communicate with our international clients (usually British or American) and organise the logistics of shooting in foreign countries.

For content inspiration, see our current website: http://www.lensharborteutonia.com - however we want to move away from the very simple structure of this site and move towards a layout that displays and allows for frequently updated content (e.g. in the form of a blog).

Here is an example of the kind of clean look we like:
http://www.qrvpixelarchive.com/archive/main/reelsqrv.do#reel=48213760

Please keep within the following specifications:
- We wish to keep our logo (grey/white, font: Glypha) and our company colour red (#C40A0A) as they are.
- Maximum Width 960px, on a large browser-window the design should be centred
- Easily readable font sizes with good contrast
- Provide your design in PSD file format
- Our logo should be graphically displayed in the top left of the header.
- The design should allow space for a video.
- The page should have a clearly recognisable end in the form of a footer.

The following menu items need to be clearly arranged so the viewer is not overwhelmed or confused:
About
Services - Crews / Corporate Shoots / Webcasts / Production Arm / Legal Videography
Recent Productions
Blog
Testimonials
Get a Quote
Contact
Film Library
Showreel
Events
Film Location Guide - Frankfurt / Cologne / Zurich / Helsinki / Amsterdam / London / Paris / Rome / Brussels / Berlin / Munich
Updates

Reason: Hi - thanks very much for your interest in our design project.  We are extending this auction because we haven't had enough time to really focus on the desigs and provide immediate feedback to designers.  We will try to provide timely feedback and are giving you more time to make any adjustments to your designs etc.
Thanks!
Marla

Target Market(s)

Our target customers are males and females between 25 and 55 years (mostly British and American). More important than their demographic though, is their occupation - they are largely communication and design savvy individuals belonging to one of the following three categories: 1)Broadcasters (usually producers for example from the QRV or Horizon Vista TV seeking trustworthy, affordable crews for their foreign shoots).

2) Video Production Companies (seeking a trustworthy, affordable partner company to provide the crews for their own corporate clients).

3) Corporate Communications Specialists (seeking professional producers and crews to facilitate production of company videos or filming of events).

Industry/Entity Type

Camera

Requirements
Must have
• A fresh clean appearance with good use of white space.
Should not have
• Avoid dark heavy colours and designs.
• Avoid designs that would be impractical and could potentially take a long time to load.

```html
<!DOCTYPE html>
<html lang="en">
<head>
<meta charset="utf-8">
<title>Lens Harbor Teutonia</title>
<link rel="stylesheet" href="https://fonts.googleapis.com/css2?family=Arvo:wght@700&family=Arimo:wght@400;700&display=swap">
<style>
:root{
  --brand-red:#c40a0a;
  --bright-red:#e8000a;
  --deep-red:#b80008;
  --menu-red:#d81e1e;
  --ink:#222;
  --body-ink:#333;
  --rule:#555;
  --steel:#4a4a4a;
  --white:#fff;
  --video-red:#dc1537;
}
*{box-sizing:border-box;margin:0;padding:0}
html,body{width:960px;height:1200px;overflow:hidden;background:var(--white);font-family:"Arimo",Arial,sans-serif;color:var(--body-ink)}
.page{position:relative;width:960px;height:1200px}
.top-strip{position:absolute;left:0;top:0;width:960px;height:8px;background:linear-gradient(#777,#333)}
.header{position:absolute;left:0;top:8px;width:960px;height:240px;background:radial-gradient(ellipse at 30% 40%,#f20a0a,var(--deep-red) 80%)}
.logo{position:absolute;left:10px;top:10px;font-family:"Arvo",Georgia,serif;font-weight:700;color:var(--white);font-size:68px;line-height:72px;letter-spacing:-2px}
.header-photo{position:absolute;left:545px;top:0;width:415px;height:240px;background:radial-gradient(ellipse at 70% 55%,#333 0,#666 35%,rgba(120,120,120,.4) 60%,rgba(200,0,0,0) 75%)}
.nav{position:absolute;left:0;top:248px;width:960px;height:38px;border-top:2px solid var(--rule);border-bottom:2px solid var(--rule);background:var(--white)}
.nav ul{list-style:none;display:flex;position:absolute;left:15px;top:10px;font-size:12px;font-weight:700;color:var(--ink)}
.nav li+li::before{content:"|";padding:0 6px;font-weight:400}
.nav .active{color:var(--brand-red);text-decoration:underline}
.flag{position:absolute;left:920px;top:10px;width:26px;height:16px}
.submenu{position:absolute;left:80px;top:275px;width:160px;height:101px;background:var(--menu-red);list-style:none;padding:7px 0 0 12px;z-index:2}
.submenu li{color:var(--white);font-size:12px;font-weight:700;line-height:18px}
.content{position:absolute;left:20px;top:316px;width:680px;font-size:13px;line-height:24px}
.content h1{font-size:21px;font-weight:700;line-height:22px;color:var(--steel);margin-bottom:32px;width:620px}
.content ul{list-style:none;padding-left:15px}
.content ul li::before{content:"* "}
.content a{color:var(--brand-red)}
.gap{height:24px}
.video{position:absolute;left:22px;top:800px;width:506px;height:320px;border:1px solid #bbb}
.video-screen{height:304px;background:var(--video-red);position:relative}
.video-title{position:absolute;left:0;right:0;top:133px;text-align:center;color:var(--white);font-family:"Arvo",Georgia,serif;font-weight:700;font-size:32px;letter-spacing:-1px}
.video-bar{height:14px;background:linear-gradient(#f4f4f4,#ccc);border-top:1px solid #999}
.like-btn{position:absolute;left:561px;top:1067px;font-size:11px;display:flex;gap:3px;align-items:center}
.like-btn .face{border:1px solid #9aa;background:#eef;padding:1px 5px;color:#3b5998;display:flex;align-items:center;gap:4px}
.like-btn .face i{width:10px;height:10px;background:#3b5998;display:block}
.like-btn .count{border:1px solid #aaa;padding:1px 4px;font-weight:700}
.follow{position:absolute;left:561px;top:1099px;border:1px solid #bbb;background:#f6f6f6;font-size:12px;padding:1px 5px;color:var(--ink)}
.follow b{color:#3ab4e0;font-weight:400}
.side-box{position:absolute;left:720px;width:240px;background:linear-gradient(var(--bright-red),var(--deep-red));color:var(--white)}
.side-box h2{font-size:54px;font-weight:700;line-height:48px;padding:6px 0 0 8px;letter-spacing:-1px}
.events{top:322px;height:214px}
.events .date{font-size:22px;font-weight:700;padding:4px 0 0 11px}
.events p{font-size:12px;line-height:19px;padding:0 10px 0 11px}
.events .more{font-weight:700;margin-top:18px}
.share{top:546px;height:110px}
.share-icons{display:flex;gap:20px;padding:8px 0 0 13px}
.share-icons span{width:46px;height:46px;border-radius:6px;background:var(--white);opacity:.9}
.quote{top:666px;height:442px}
.quote h2{line-height:46px}
.quote form{padding:10px 0 0 9px;font-size:12px}
.quote label{display:block;line-height:16px}
.quote .field{width:190px;height:17px;background:var(--white);border:1px solid #888;margin:1px 0 2px}
.quote .message{height:131px}
.buttons{display:flex;justify-content:space-between;width:190px;margin-top:3px;padding-left:2px}
.buttons span{width:74px;height:29px;background:linear-gradient(#666,#111);font-size:12px;text-align:center;line-height:29px}
.note{font-size:12px;line-height:18px;margin-top:5px}
.footer{position:absolute;left:0;top:1162px;width:960px;height:30px;background:var(--brand-red);color:var(--white);font-size:12px;padding:8px 0 0 19px}
.bottom-strip{position:absolute;left:0;top:1192px;width:960px;height:8px;background:linear-gradient(#555,#888)}
</style>
</head>
<body>
<div class="page">
  <div class="top-strip"></div>
  <header class="header">
    <div class="logo">lens<br>harbor<br>teutonia</div>
    <div class="header-photo" role="img" aria-label="Photo of professional video cameras on a tripod"></div>
  </header>
  <nav class="nav">
    <ul>
      <li>About Us</li><li class="active">Our Services</li><li>Recent Productions</li><li>Blog</li><li>Testimonials</li><li>Get a Quote</li><li>Contact</li><li>Film Library</li><li>Showreel</li><li>Film Location Guide</li>
    </ul>
    <svg class="flag" viewBox="0 0 26 16" aria-label="German language"><rect width="26" height="5.4" fill="#000"/><rect y="5.3" width="26" height="5.4" fill="#d00"/><rect y="10.6" width="26" height="5.4" fill="#fc0"/></svg>
  </nav>
  <ul class="submenu">
    <li>Crews</li><li>Corporate Shoots</li><li>Webcasts</li><li>Production Arm</li><li>Legal Videography</li>
  </ul>
  <main class="content">
    <h1>english speaking camera crews throughout germany and europe</h1>
    <p>We set up Lens Harbor Teutonia to meet the demands of a growing number of TV-producers whose working language is English. This is our Passion! Why else would we keep doing it for over 30 years!<br>
    As a producer, you're bound to have great ideas…but how do you make them a reality in a country where you can't speak the language? Partner with us!<br>
    We are native English speakers so nothing gets lost in translation. We'll catch hold of your vision, and with local know-how, we'll make it happen.</p>
    <div class="gap"></div>
    <p>No job is too big, too small, too hard, too far away, or too urgent. Try us!</p>
    <ul>
      <li>We provide camera crews and facilities throughout Germany and Europe</li>
      <li>We shoot in both PAL and NTSC</li>
      <li>We edit either in-studio or on the move and we transfer urgent footage via FTP or SNG</li>
      <li>We are on call 24/7</li>
    </ul>
    <div class="gap"></div>
    <p>To make a no obligation enquiry about any of our services, please call<br>
    Frankfurt Headquarters: +49-69-417253 (Toll free from the USA 1-866-555-0142)<br>
    or click here to <a href="#">get a quote</a>.</p>
  </main>
  <div class="video">
    <div class="video-screen">
      <div class="video-title">lensharborteutonia</div>
      <svg style="position:absolute;left:237px;top:136px" width="32" height="32" viewBox="0 0 32 32" aria-label="Play"><rect width="32" height="32" fill="#7a0010"/><path d="M11 8l13 8-13 8z" fill="#fff"/></svg>
    </div>
    <div class="video-bar"></div>
  </div>
  <div class="like-btn"><span class="face"><i></i>Like</span><span class="count">4</span></div>
  <div class="follow">Follow us on <b>Chirpline</b></div>
  <aside>
    <section class="side-box events">
      <h2>events</h2>
      <div class="date">03.11.2010</div>
      <p>Lorem ipsum dolor sit amet, consectetur adipisicing elit, sed do eiusmod tempor incididunt ut labore et dolore.....</p>
      <p class="more">&gt;&gt;&gt; See All</p>
    </section>
    <section class="side-box share">
      <h2>share</h2>
      <div class="share-icons">
        <span aria-label="Circlebook"></span><span aria-label="Chirpline"></span><span aria-label="ClipStream"></span>
      </div>
    </section>
    <section class="side-box quote">
      <h2>get a<br>quote</h2>
      <form>
        <label>NAME</label><div class="field"></div>
        <label>EMAIL</label><div class="field"></div>
        <label>CONTACT NUMBER</label><div class="field"></div>
        <label>MESSAGE</label><div class="field message"></div>
        <div class="buttons"><span>SEND</span><span>CLEAR</span></div>
        <p class="note">+ A copy of this message will be sent<br>&nbsp;&nbsp;&nbsp;to the address you have specified.</p>
      </form>
    </section>
  </aside>
  <footer class="footer">Copyright - 2010 - Privacy Policy &nbsp;|&nbsp; Terms and Conditions &nbsp;|&nbsp; Contact Us</footer>
  <div class="bottom-strip"></div>
</div>
</body>
</html>
```